Environmental Plastics Infographic on Marine Debris

We need a series of infographics that can be used individually or as a combined presentation. We'd like the combined piece to include an introduction and conclusion along with 4-5 infographics. Each infographic (information unit) should also work as a standalone. We are trying to help people visualize size proportions and ratios to put the plastics marine debris problem in perspective. Our key point is concerning polystyrene foam which represents 35 tons. We are looking for something creative to help people understand what the problem represents in terms they are familiar with.

To view our typical company design/style please see our website at www.brantleyfoamworks.org. Our primary RGB colors are: (187,140,9); (94,47,29); (94,138,164); and (164,167,15). Secondary RGB colors are (249,162,28) and (218,210,208). Our title/header font is DIN Next LT Pro and our copy font is Calibri 10.5 pt. We can deviate from the font specification if beneficial and welcome interesting text treatments and typography.

Need extra days to review

Target Market(s)

international brand manufacturers (corvantel, makiro), US legislators & government agencies

Font styles to use
Sans Serif

Requirements
Must have
• Sufficient white space. Easy to grasp message concept with visual components.

```html
<!DOCTYPE html>
<html lang="en">
<head>
<meta charset="utf-8">
<title>GPGP Plastics Mass Breakdown</title>
<link rel="stylesheet" href="https://fonts.googleapis.com/css2?family=Open+Sans:wght@400;700&display=swap">
<style>
  :root {
    --bg: #dbd3d1;
    --ink: #0f2a36;
    --accent: #ef7421;
    --pie: #f7a21e;
    --pie-edge: #ea7317;
    --icon-zone: #e8921b;
    --rule: #1f4a63;
    --sea-light: #a3b0b9;
    --sea-deep: #22506a;
    --sea-far: #52809b;
  }
  * { margin: 0; padding: 0; box-sizing: border-box; }
  html, body { width: 1200px; height: 900px; overflow: hidden; background: var(--bg); }
  .infographic {
    position: relative; width: 1200px; height: 900px; overflow: hidden;
    background: var(--bg); font-family: "Open Sans", Arial, sans-serif; color: var(--ink);
  }
  .artwork { position: absolute; inset: 0; }
  .headline {
    position: absolute; right: 680px; top: 30px; text-align: right;
    font-size: 41px; line-height: 54px; font-weight: 400; letter-spacing: 0.5px;
  }
  .headline strong { font-weight: 700; }
  .stat { position: absolute; text-align: center; font-size: 26px; line-height: 36px; }
  .stat .figure { color: var(--accent); font-weight: 700; font-size: 58px; line-height: 60px; }
  .stat--gear { left: 58px; width: 300px; top: 248px; }
  .stat--hard { left: 58px; width: 330px; top: 556px; }
  .stat--foam { left: 790px; width: 260px; top: 48px; }
  .stat--foam .figure { display: block; font-size: 60px; line-height: 66px; }
</style>
</head>
<body>
<main class="infographic">
  <svg class="artwork" width="1200" height="900" viewBox="0 0 1200 900">
    <defs>
      <linearGradient id="sea" x1="0" y1="0" x2="1" y2="0">
        <stop offset="0" stop-color="var(--sea-deep)"/>
        <stop offset="1" stop-color="var(--sea-far)"/>
      </linearGradient>
      <clipPath id="quadrant-top-left">
        <path d="M754,428 L470,428 A294,294 0 0 1 754,144 Z"/>
      </clipPath>
    </defs>
    <path class="wave-crest" d="M0,756 C300,748 500,676 700,576 C850,498 1000,424 1200,426 L1200,900 L0,900 Z" fill="var(--sea-light)"/>
    <path class="wave-body" d="M0,782 C300,772 500,702 700,602 C850,524 1000,452 1200,452 L1200,900 L0,900 Z" fill="url(#sea)"/>

    <g class="pie-chart">
      <path d="M764,438 L452,438 A312,312 0 0 1 764,126 Z" fill="var(--pie-edge)" transform="translate(-6,5)"/>
      <path d="M764,438 L452,438 A312,312 0 0 1 764,126 Z" fill="var(--pie)"/>
      <path d="M764,446 L764,758 A312,312 0 0 1 452,446 Z" fill="var(--pie-edge)" transform="translate(-6,5)"/>
      <path d="M764,446 L764,758 A312,312 0 0 1 452,446 Z" fill="var(--pie)"/>
      <path d="M772,446 L1084,446 A312,312 0 0 1 772,758 Z" fill="var(--pie-edge)" transform="translate(-6,5)"/>
      <path d="M772,446 L1084,446 A312,312 0 0 1 772,758 Z" fill="var(--pie)"/>
    </g>

    <rect class="icon-zone" x="526" y="162" width="220" height="240" rx="10" fill="var(--icon-zone)" clip-path="url(#quadrant-top-left)" role="img" aria-label="Fishing rod with line and hooks"/>
    <rect class="icon-zone" x="534" y="472" width="170" height="178" rx="10" fill="var(--icon-zone)" role="img" aria-label="Two plastic jugs"/>
    <rect class="icon-zone" x="832" y="498" width="126" height="172" rx="10" fill="var(--icon-zone)" role="img" aria-label="Foam cup"/>

    <g class="callouts" fill="none" stroke="var(--rule)" stroke-width="4">
      <polyline points="512,318 436,318 436,391 62,391"/>
      <circle cx="536" cy="318" r="24" stroke-width="6"/>
      <polyline points="1038,466 1038,337 804,337"/>
      <circle cx="1038" cy="490" r="24" stroke-width="6"/>
      <polyline points="698,698 506,698 506,733 62,733"/>
      <circle cx="722" cy="698" r="24" stroke-width="6"/>
    </g>
  </svg>

  <h1 class="headline">The total plastics mass in<br>the GPGP is projected at<br><strong>78,908 tons</strong></h1>

  <p class="stat stat--gear"><span class="figure">52%</span> is mostly<br>abandoned fishing gear;<br>not consumer plastics</p>

  <p class="stat stat--hard"><span class="figure">47%</span> is hard plastics,<br>sheets, and film,<br>making up the majority of<br>microplastics mass</p>

  <p class="stat stat--foam"><span class="figure">0.05%</span>is foamed plastics,<br>including<br>polystyrene,<br>making it a minor<br>component of the<br>GPGP</p>
</main>
</body>
</html>
```